Admin Backend Redesign

We need a redesign for our backend which supoosed to make the backoffice look more modern!

I will add screenshots of the backoffice so you know what data will be shown in the Admin.

Have in mind that the users of this backend are Doctors. We need a clinical look, modern and sharp. The backoffice is responsive, have that in mind. We need the backoffice to look as professional as possible.

The theme used for the website is: http://velmora.quillstack-sample.com/

ON the main page of the backoffice, under every widget i need some space to write an explanation what the widget is about.

The color code used in our logo and website is #57aad4 combined with white.

We are open for ideas!
Updates

Project Deadline Extended
Reason: Designs are ok, but nothing innovative. Please use more modern designs!

Project Deadline Extended
Reason: Havent recieved a perfect design yet. Please read instructions carefully! Thank you

Project Deadline Extended
Reason: Hey everybody, sorry for the delay. We will decide in 3 days. If anyone wants to add a Design, that would be great.

Target Market(s)

Doctors, therapists

Industry/Entity Type

It Professional

Font styles to use
Sans Serif

Requirements
Must have
• Must look uptodate, modern, like new back offices look nowadays

```html
<!DOCTYPE html>
<html lang="en">
<head>
<meta charset="utf-8">
<title>Admin – Inner page</title>
<link rel="stylesheet" href="https://fonts.googleapis.com/css2?family=Open+Sans:wght@400;600;700&display=swap">
<style>
:root{
  --brand:#57aad4;
  --side:#3b8db8;
  --side-dark:#2f7ea9;
  --deep:#1a6e9c;
  --footer:#125a80;
  --accent:#e8505b;
  --label:#5a5f66;
  --muted:#8a9199;
  --field:#dcdcdc;
  --crumb:#f5f5f5;
  --grey-btn:#a3a3a3;
}
*{box-sizing:border-box;margin:0;padding:0}
html,body{width:1200px;height:1125px;overflow:hidden;background:#fff;font-family:"Open Sans",Arial,sans-serif;color:var(--label)}
.canvas{position:relative;width:1200px;height:1125px}
.topbar{position:absolute;left:0;top:0;width:1200px;height:45px;background:var(--brand)}
.brand{position:absolute;left:105px;top:9px;color:#fff;font-size:21px;font-weight:400;letter-spacing:-.5px}
.user{position:absolute;right:160px;top:11px;color:#fff;font-size:19px;display:flex;align-items:center;gap:12px}
.divider{position:absolute;left:1041px;top:0;width:1px;height:45px;background:rgba(255,255,255,.35)}
.settings{position:absolute;left:1053px;top:12px}
.sidebar{position:absolute;left:105px;top:66px;width:216px;height:304px;background:var(--side);border-radius:3px}
.sidebar::before{content:"";position:absolute;left:25px;top:-10px;border:10px solid transparent;border-top:0;border-bottom-color:var(--side)}
.menu-btn{position:absolute;left:171px;top:9px;width:37px;height:27px;background:var(--side-dark);border-radius:3px;display:flex;align-items:center;justify-content:center}
.nav-item{position:absolute;left:0;width:216px;display:flex;align-items:center;gap:12px;font-size:16px;color:#fff;padding-left:9px}
.nav-item.dash{top:53px}
.nav-item.current{top:89px;height:39px;background:#fff;color:#555;font-size:15px}
.nav-item.lorem{top:143px;padding-left:10px;gap:16px;font-size:15px}
.crumbs{position:absolute;left:352px;top:68px;width:738px;height:38px;background:var(--crumb);border-radius:4px;display:flex;align-items:center;padding-left:15px;gap:8px;font-size:13px;color:#444}
.page-title{position:absolute;left:357px;top:148px;color:var(--accent);font-size:23px;font-weight:400}
.page-intro{position:absolute;left:357px;top:186px;font-size:11px;line-height:17px;color:var(--muted)}
.add-btn{position:absolute;left:906px;top:139px;width:183px;height:41px;background:var(--side);border-radius:3px;color:#fff;font-size:16px;display:flex;align-items:center}
.add-btn span{flex:1;padding-left:9px}
.add-btn i{width:52px;height:41px;background:var(--deep);border-radius:0 3px 3px 0;display:flex;align-items:center;justify-content:center}
.field label{position:absolute;font-size:12.5px;color:var(--label)}
.input{position:absolute;width:263px;height:42px;border:2px solid var(--field);border-radius:3px;font-size:11px;color:#aaa;padding:12px 9px}
.caret{position:absolute;right:10px;top:16px;border:7px solid transparent;border-top:7px solid #d3d3d3;border-bottom:0}
.status{position:absolute;left:724px;top:843px;display:flex;gap:5px}
.status b{width:8px;height:8px;border-radius:50%}
.btn{position:absolute;top:915px;height:38px;border-radius:3px;color:#fff;font-size:12.5px;font-weight:700;letter-spacing:.6px;display:flex;align-items:center;justify-content:center}
.btn.register{left:848px;width:120px;background:var(--deep)}
.btn.cancel{left:972px;width:101px;background:var(--grey-btn)}
.footer{position:absolute;left:0;top:1090px;width:1200px;height:35px;background:var(--footer)}
</style>
</head>
<body>
<div class="canvas">
  <header class="topbar">
    <div class="brand">Logo here</div>
    <div class="user">
      <svg width="15" height="17" viewBox="0 0 15 17"><circle cx="7.5" cy="4.5" r="4" fill="#fff"/><path d="M0 17c0-5 3-8 7.5-8S15 12 15 17z" fill="#fff"/></svg>
      Dr.Lena Varo
    </div>
    <div class="divider"></div>
    <svg class="settings" width="20" height="20" viewBox="0 0 20 20"><g fill="#fff"><circle cx="10" cy="10" r="7"/><rect x="8" y="0" width="4" height="20" rx="1"/><rect x="0" y="8" width="20" height="4" rx="1"/><rect x="8" y="0" width="4" height="20" rx="1" transform="rotate(45 10 10)"/><rect x="8" y="0" width="4" height="20" rx="1" transform="rotate(-45 10 10)"/></g><circle cx="10" cy="10" r="3.2" fill="var(--brand)"/></svg>
  </header>

  <nav class="sidebar">
    <div class="menu-btn"><svg width="16" height="12" viewBox="0 0 16 12"><g fill="#fff"><rect y="1" width="16" height="2"/><rect y="5" width="16" height="2"/><rect y="9" width="16" height="2"/></g></svg></div>
    <div class="nav-item dash"><svg width="17" height="15" viewBox="0 0 17 15"><path d="M8.5 0L0 7.5h2.5V15h4.5v-5h3v5h4.5V7.5H17z" fill="#fff"/></svg>Dashboard</div>
    <div class="nav-item current"><svg width="15" height="16" viewBox="0 0 15 17"><circle cx="7.5" cy="4.5" r="4" fill="#aaa"/><path d="M0 17c0-5 3-8 7.5-8S15 12 15 17z" fill="#aaa"/></svg>Pnteger ornare libero</div>
    <div class="nav-item lorem"><svg width="15" height="16" viewBox="0 0 15 17"><circle cx="7.5" cy="4.5" r="4" fill="#fff"/><path d="M0 17c0-5 3-8 7.5-8S15 12 15 17z" fill="#fff"/></svg>Lorem ipsum libero</div>
  </nav>

  <div class="crumbs">
    <svg width="14" height="13" viewBox="0 0 17 15"><path d="M8.5 0L0 7.5h2.5V15h4.5v-5h3v5h4.5V7.5H17z" fill="#b5b5b5"/></svg>
    <span>Dashboard</span>
    <svg width="8" height="10" viewBox="0 0 8 10"><path d="M2 1l4 4-4 4" stroke="#777" fill="none"/></svg>
    <span>Inner page2</span>
  </div>

  <h1 class="page-title">Lorem ipsum</h1>
  <p class="page-intro">Integer ornare libero nisi. Duis ac magna urna.<br>Nulla facilisi. Phasellus at ante magna.</p>
  <div class="add-btn"><span>Add lorem ipsum</span><i><svg width="16" height="16" viewBox="0 0 16 16"><path d="M6 0h4v6h6v4h-6v6H6v-6H0V6h6z" fill="#fff"/></svg></i></div>

  <form class="form">
    <div class="field"><label style="left:357px;top:238px">Country</label><div class="input" style="left:357px;top:261px">Egypt<span class="caret"></span></div></div>
    <div class="field"><label style="left:724px;top:238px">Country</label><div class="input" style="left:724px;top:261px">Egypt</div></div>
    <div class="field"><label style="left:357px;top:314px">Username</label><div class="input" style="left:357px;top:337px">M-Harlow</div></div>
    <div class="field"><label style="left:724px;top:314px">Username</label><div class="input" style="left:724px;top:337px">M-Harlow</div></div>
    <div class="field"><label style="left:357px;top:393px">Password</label><div class="input" style="left:357px;top:416px"></div></div>
    <div class="field"><label style="left:724px;top:393px">Password</label><div class="input" style="left:724px;top:416px"></div></div>
    <div class="field"><label style="left:357px;top:473px">Re-Password</label><div class="input" style="left:357px;top:496px"></div></div>
    <div class="field"><label style="left:724px;top:473px">Re-Password</label><div class="input" style="left:724px;top:496px"></div></div>
    <div class="field"><label style="left:357px;top:557px">Country</label><div class="input" style="left:357px;top:580px">Egypt</div></div>
    <div class="field"><label style="left:724px;top:557px">Country</label><div class="input" style="left:724px;top:580px">Egypt<span class="caret"></span></div></div>
    <div class="field"><label style="left:357px;top:643px">Password</label><div class="input" style="left:357px;top:666px"></div></div>
    <div class="field"><label style="left:724px;top:643px">Password</label><div class="input" style="left:724px;top:666px"></div></div>
    <div class="field"><label style="left:357px;top:722px">Re-Password</label><div class="input" style="left:357px;top:745px"></div></div>
    <div class="field"><label style="left:724px;top:722px">Re-Password</label><div class="input" style="left:724px;top:745px"></div></div>
    <div class="field"><label style="left:357px;top:807px">Website</label><div class="input" style="left:357px;top:830px">Egypt</div></div>
    <div class="field"><label style="left:724px;top:807px">Online status</label></div>
    <div class="status"><b style="background:#3d4650"></b><b style="background:#ddd"></b><b style="background:#22e01a"></b></div>
    <div class="btn register">REGISTER</div>
    <div class="btn cancel">CANCEL</div>
  </form>

  <footer class="footer"></footer>
</div>
</body>
</html>
```